Vordaline - Fitness Coach. Needs a Business Card Design that I can also use for other advertising

Established 2012, I have finished the KTRB National Certificate in Fitness & Personal Training. Harlow Cross First Aid Certificate. I have the Auckland 800m track records for MW45. I also came 1st at the 2012 Pellamar Games in 800 & 1500m. I am passionate about health & fitness and would like to help people reach their health & fitness goals. I also take health & fitness weekends. Main interests - Running, Weight Training, Yoga & Aqua Jogging. I like strength/power, but am femine.

Target Market(s)

Male or Female 18 and over that wants to improve their health & fitness

Industry/Entity Type

Advertising

Requirements
Must have
• my name: Rosalind K Tarbury contact details: ros@quillsend.co.nz mobile - 021 583917 URL name: facebook.com/rosalindKtarbury - VordaLine
Photo of Me

```html
<!DOCTYPE html>
<html lang="en">
<head>
<meta charset="utf-8">
<title>Rosalind K Tarbury – Personal Trainer Business Card</title>
<link rel="stylesheet" href="https://fonts.googleapis.com/css2?family=Chewy&family=PT+Sans:wght@400;700&family=Roboto+Condensed:wght@700&family=Parisienne&display=swap">
<style>
  :root {
    --bg: #e6e6e6;
    --green-light: #8fd35a;
    --green-mid: #3fae3a;
    --green-deep: #1e8f3a;
    --green-ink: #0f5a22;
    --frame: #1d1b1c;
    --white: #ffffff;
    --text-dark: #1a2a1a;
    --photo-top: #2f4a25;
    --photo-mid: #4f7a36;
    --photo-lawn: #6fae3e;
  }
  * { box-sizing: border-box; margin: 0; padding: 0; }
  html, body {
    width: 1200px; height: 646px; overflow: hidden;
    background: var(--bg);
  }
  .canvas {
    position: relative; width: 1200px; height: 646px;
    display: flex; align-items: center; justify-content: center; gap: 40px;
  }
  .card {
    position: relative; width: 540px; height: 330px; overflow: hidden;
    box-shadow: 0 6px 18px rgba(0,0,0,.18);
  }

  /* Back side */
  .card-back {
    background: radial-gradient(ellipse at 50% 45%, var(--green-light) 0%, var(--green-mid) 45%, var(--green-deep) 100%);
    color: var(--white);
    padding: 92px 60px 0 60px;
  }
  .card-back .bio {
    font-family: "PT Sans", sans-serif;
    font-size: 15px; line-height: 1.3;
  }
  .card-back .signature {
    font-family: "Parisienne", cursive;
    font-size: 24px; text-align: right; margin-top: 12px; padding-right: 10px;
  }

  /* Front side */
  .card-front { display: flex; background: var(--frame); }
  .front-panel {
    width: 262px; height: 100%; padding: 14px;
  }
  .front-panel-inner {
    width: 100%; height: 100%;
    background: radial-gradient(ellipse at 50% 40%, var(--green-light) 0%, var(--green-mid) 50%, var(--green-deep) 100%);
    padding: 26px 16px 0 18px;
  }
  .role {
    font-family: "PT Sans", sans-serif; font-weight: 700;
    font-size: 13px; color: var(--text-dark); margin-left: 10px;
  }
  .name {
    font-family: "Chewy", cursive; color: var(--white);
    font-size: 38px; line-height: .95; margin-top: 6px;
    -webkit-text-stroke: 1.5px var(--green-ink);
    text-shadow: 0 0 0 var(--green-ink), 2px 2px 0 var(--green-ink);
  }
  .name .line2 { display: block; padding-left: 56px; }
  .contact {
    list-style: none; margin-top: 26px;
    font-family: "Roboto Condensed", sans-serif; font-weight: 700;
    font-size: 16px; line-height: 1.3; color: var(--white);
  }
  .photo {
    flex: 1; height: 100%;
    background: linear-gradient(180deg, var(--photo-top) 0%, var(--photo-mid) 65%, var(--photo-lawn) 100%);
  }
</style>
</head>
<body>
  <main class="canvas">
    <section class="card card-back">
      <p class="bio">KTRB National Certificate in Fitness &amp; Personal Training, Harlow Cross First Aid Certificate. I have the Auckland 800m track records for MW45. I also came 1st at the 2012 Pellamar Games in 800 &amp; 1500m. I am passionate about health &amp; fitness and would like to help people reach their health &amp; fitness goals.</p>
      <p class="signature">Rosalind K Tarbury</p>
    </section>

    <section class="card card-front">
      <div class="front-panel">
        <div class="front-panel-inner">
          <p class="role">Personal Trainer</p>
          <h1 class="name">Rosalind K <span class="line2">Tarbury</span></h1>
          <ul class="contact">
            <li>ros@quillsend.co.nz</li>
            <li>mobile - 021 583917</li>
            <li>facebook - Vordaline</li>
          </ul>
        </div>
      </div>
      <div class="photo" role="img" aria-label="Photo of the trainer leaping in the air in front of a green hedge on a lawn"></div>
    </section>
  </main>
</body>
</html>
```